Love-Drama Movie Flyer for World Sales Pitch

Dear Designers

We need for a world sales pitch a flyer for our new movie MARBLEFIN. We need a front and a back page A4.
Front: One picture we deliver for then whole page, title, some "pitch" sentences
Picture Front: https://www.fileharbor-example.net/s/qk83tnb2px71vd9/Front_Picture.jpg?dl=0
Back: Arrangement of title, 5 pictures and text we deliver (attached)

Please find in the attached examples a rough idea what we’re looking for. Should not be exactly the same.

To get an Impression of the content and style of the film, please watch the 3min teaser. This will be very important for the style of the flyer:
https://clipvault-example.net/487316920
pw: tutumarblefin

In the end we prefer a data package with the flyer made in a adobe design application for high quality print.

Thanks
Tomas Vrelnik
Producer

Target Market(s)

High profile film sales professionals

Industry/Entity Type

Film Production

Requirements
Must have
• see description
Should not have
• not too generic,
• there is the color red on the actors pullover but red is not really a color in the film. So please don't use much red
• Awards of the actor/actress are not for this movie, it's from other movies

```html
<!DOCTYPE html>
<html lang="en">
<head>
<meta charset="utf-8">
<title>MARBLEFIN – Flyer Front</title>
<link href="https://fonts.googleapis.com/css2?family=Antonio:wght@200;400&family=Montserrat:ital,wght@0,400;0,500;1,400;1,500&family=Six+Caps&display=swap" rel="stylesheet">
<style>
  :root {
    --bg: #0b0b0c;
    --photo-light: #3a3a3d;
    --photo-mid: #2a2a2d;
    --photo-dark: #161618;
    --accent: #e0875a;
    --text-light: #e4e0d6;
    --text-muted: #d2d2d2;
    --ink: #141414;
  }
  html, body {
    margin: 0;
    padding: 0;
    width: 848px;
    height: 1200px;
    overflow: hidden;
    background: var(--bg);
  }
  .flyer {
    position: relative;
    width: 848px;
    height: 1200px;
    overflow: hidden;
    background: radial-gradient(ellipse 520px 760px at 600px 520px, #1a1a1c 0%, var(--bg) 80%);
    font-family: "Montserrat", Arial, sans-serif;
  }
  .key-photo {
    position: absolute;
    left: 300px;
    top: 140px;
    width: 528px;
    height: 1060px;
    border-radius: 200px 200px 0 0;
    background:
      radial-gradient(ellipse 110px 150px at 290px 190px, #5a4a42 0%, rgba(90,74,66,0) 100%),
      linear-gradient(180deg, var(--photo-light) 0%, var(--photo-mid) 45%, var(--photo-dark) 100%);
  }
  .credit {
    position: absolute;
    left: 32px;
    margin: 0;
    white-space: nowrap;
  }
  .credit-title {
    display: block;
    font-style: italic;
    font-weight: 500;
    font-size: 26px;
    line-height: 1;
    color: var(--accent);
    letter-spacing: -0.4px;
  }
  .credit-note {
    display: block;
    font-style: italic;
    font-weight: 400;
    font-size: 17px;
    line-height: 1.2;
    color: var(--text-light);
    margin-top: 4px;
    text-transform: uppercase;
    letter-spacing: -0.3px;
  }
  .credit--first { top: 76px; }
  .credit--second { top: 176px; }
  .credit--series {
    top: 232px;
    font-style: italic;
    font-weight: 500;
    font-size: 17px;
    line-height: 31px;
    color: var(--text-light);
    letter-spacing: -0.3px;
  }
  .credit--series .series-name {
    font-size: 24px;
    font-weight: 400;
    color: var(--accent);
    font-style: normal;
  }
  .credit--lead-f { left: 38px; }
  .credit--third { top: 592px; }
  .credit--fourth { top: 695px; }
  .credit--fifth { top: 797px; }

  .tagline {
    position: absolute;
    left: 32px;
    top: 404px;
    margin: 0;
    font-family: "Antonio", "Arial Narrow", sans-serif;
    font-weight: 200;
    font-size: 56px;
    line-height: 1;
    letter-spacing: 16px;
    word-spacing: 18px;
    color: var(--text-light);
    white-space: nowrap;
  }
  .cast-band {
    position: absolute;
    left: 32px;
    top: 894px;
    width: 784px;
    height: 47px;
    background: var(--accent);
    display: flex;
    justify-content: space-between;
    align-items: center;
    padding: 0 26px;
    box-sizing: border-box;
  }
  .cast-name {
    font-family: "Antonio", "Arial Narrow", sans-serif;
    font-weight: 400;
    font-size: 32px;
    letter-spacing: 5px;
    color: var(--ink);
    text-transform: uppercase;
  }
  .film-title {
    position: absolute;
    left: 50px;
    top: 990px;
    margin: 0;
    font-family: "Six Caps", "Arial Narrow", sans-serif;
    font-weight: 400;
    font-size: 150px;
    line-height: 1;
    letter-spacing: 3px;
    color: var(--accent);
  }
  .director {
    position: absolute;
    left: 52px;
    top: 1136px;
    margin: 0;
    font-size: 26px;
    color: var(--text-muted);
  }
  .release {
    position: absolute;
    right: 56px;
    top: 996px;
    margin: 0;
    font-weight: 500;
    font-size: 30px;
    color: var(--accent);
    text-align: right;
  }
  .website {
    position: absolute;
    right: 56px;
    top: 1045px;
    margin: 0;
    font-size: 20px;
    color: var(--text-muted);
    text-align: right;
  }
</style>
</head>
<body>
<main class="flyer">
  <div class="key-photo" role="img" aria-label="Photo of the lead actor in a dark grey hooded sweatshirt, hood up, standing against a black background with hands in the front pocket"></div>

  <p class="credit credit--first"><span class="credit-title">ALPINE SCREEN AWARD 2015</span><span class="credit-note">Best Actor (for The Ring Road)</span></p>
  <p class="credit credit--second"><span class="credit-title">CONTINENTAL RISING STAR 2015</span></p>
  <p class="credit credit--series">RECURRING APPEARANCE IN THE<br>AWARD WINNING US SERIES <span class="series-name">BORDERLINE</span></p>

  <h2 class="tagline">THIS IS DAVID</h2>

  <p class="credit credit--lead-f credit--third"><span class="credit-title">ORBIT AWARD NOMINEE 2016</span><span class="credit-note">Best Actress (for Summer Letters)</span></p>
  <p class="credit credit--lead-f credit--fourth"><span class="credit-title">SOUTHLAND FILM AWARD 2015</span><span class="credit-note">Best Young Actress (for Summer Letters)</span></p>
  <p class="credit credit--lead-f credit--fifth"><span class="credit-title">FRESH TALENT AWARD 2012</span><span class="credit-note">Best Actress (for Helena)</span></p>

  <div class="cast-band">
    <span class="cast-name">Luca Brenner</span>
    <span class="cast-name">Mira Solveig Hart</span>
  </div>

  <h1 class="film-title">MARBLEFIN</h1>
  <p class="director">a film by Adrian Kessel</p>

  <p class="release">COMING FALL 2016</p>
  <p class="website">www.lanternway-films.example</p>
</main>
</body>
</html>
```